Ember Roast specialty coffee shop business card

Please use Design #4817053 from previous project (logo design). Ember Roast is a new coffee shop that will serve specialty coffee and will focus on high quality products. I would like to use orange and brown colors. I like designs that are simple but elegant and that deliver a message that is easy to recognize. I will upload a file of the logo design.

Industry/Entity Type

Coffee Shop

Contact Information for Business Card

Lina Marwestil
(602) 555-0172

Font styles to use
Serif
Sans Serif
Script

Requirements
Must have
• simple and elegant, colors match nicely, I like to use orange and brown. Background creme color.
Should not have
• complex designs that are hard to understand.

```html
<!DOCTYPE html>
<html lang="en">
<head>
<meta charset="utf-8">
<title>Ember Roast – Business Card</title>
<link rel="stylesheet" href="https://fonts.googleapis.com/css2?family=Source+Sans+3:wght@400;600&display=swap">
<style>
  :root {
    --page-bg: #e4e2df;
    --card-cream: #f8f5ef;
    --brown-dark: #5a3a20;
    --brown-mid: #7a5234;
    --tan: #c9a071;
    --rule: #9c6a3c;
    --text-grey: #6b6560;
    --bean-dark: #4a2e1c;
    --bean-light: #d8d0c4;
  }
  * { margin: 0; padding: 0; box-sizing: border-box; }
  html, body {
    width: 1200px; height: 1000px; overflow: hidden;
    background: var(--page-bg);
    font-family: "Source Sans 3", sans-serif;
  }
  .canvas { position: relative; width: 1200px; height: 1000px; }
  .card {
    position: absolute; top: 355px;
    width: 510px; height: 291px;
    background: var(--card-cream);
    box-shadow: 0 6px 18px rgba(0,0,0,0.18);
    overflow: hidden;
  }
  .card--front { left: 55px; }
  .card--back { left: 635px; }

  .brand {
    position: absolute; display: flex; align-items: center; gap: 9px;
    color: var(--brown-dark); font-weight: 600; white-space: nowrap;
  }
  .brand__dot { width: 13px; height: 13px; border-radius: 50%; background: var(--tan); flex: none; }
  .card--front .brand { left: 30px; top: 126px; font-size: 26px; }
  .card--back .brand { left: 55px; top: 120px; font-size: 32px; }

  .divider {
    position: absolute; left: 235px; top: 56px;
    width: 2px; height: 178px; background: var(--rule);
  }

  .details { position: absolute; left: 262px; top: 58px; }
  .details__name { color: var(--brown-dark); font-size: 19px; line-height: 1.2; }
  .details__role { color: var(--tan); font-size: 12.5px; margin-top: 2px; }
  .details__blurb { color: var(--text-grey); font-size: 12.5px; line-height: 1.35; margin-top: 24px; }
  .contacts { list-style: none; margin-top: 14px; }
  .contacts li {
    display: flex; align-items: center; gap: 7px;
    color: var(--text-grey); font-size: 12.5px; line-height: 1.35;
  }
  .contacts svg { width: 9px; height: 9px; fill: var(--brown-mid); flex: none; }

  .photo {
    position: absolute; right: 0; top: 0; width: 300px; height: 100%;
    background:
      radial-gradient(ellipse 140px 110px at 70% 62%, var(--bean-dark) 0%, rgba(74,46,28,0.75) 45%, rgba(74,46,28,0) 100%),
      linear-gradient(to right, var(--card-cream) 0%, rgba(248,245,239,0) 40%),
      linear-gradient(to bottom, #efebe5 0%, var(--bean-light) 100%);
  }
</style>
</head>
<body>
<main class="canvas">
  <section class="card card--front" aria-label="Business card front">
    <div class="brand"><span class="brand__dot"></span>Ember Roast</div>
    <div class="divider"></div>
    <div class="details">
      <p class="details__name">Lina Marwestil</p>
      <p class="details__role">designation</p>
      <p class="details__blurb">Lorem ipsum dolor sit amet,<br>consectetur adipiscing elit.<br>Donec accumsan.</p>
      <ul class="contacts">
        <li><svg viewBox="0 0 10 10"><path d="M2 0.5 L4 0.5 L4.5 3 L3.3 3.8 Q4.3 5.9 6.2 6.7 L7 5.5 L9.5 6 L9.5 8 Q9.5 9.5 8 9.5 Q1 8.8 0.5 2 Q0.5 0.5 2 0.5Z"/></svg>(602) 555-0172</li>
        <li><svg viewBox="0 0 10 10"><rect x="0" y="1.5" width="10" height="7" rx="1"/></svg>hello@emberroast.com</li>
        <li><svg viewBox="0 0 10 10"><path d="M1 9 L9 1 M4 1 L9 1 L9 6" stroke="#7a5234" stroke-width="1.6" fill="none"/></svg>emberroast.com</li>
      </ul>
    </div>
  </section>

  <section class="card card--back" aria-label="Business card back">
    <div class="photo" role="img" aria-label="Photograph of roasted coffee beans on a weathered wooden table"></div>
    <div class="brand"><span class="brand__dot"></span>Ember Roast</div>
  </section>
</main>
</body>
</html>
```